Business Card design for Property Developer

We need a business card design for a Melbourne based Property Developer called "Kestrelmoor Holdings Pty Ltd".

We subdivide land and onsell to builders etc.

We already have a company logo, which is attached. Also I have attached the layout requirements from the printer. We would like a 2-sided design with one side displaying our logo by itself and the other with the required info, such as name, address, tel no., email, abn etc. The card will need to be used by 4 members of staff so name and contact details should be interchangable.
Updates

If possible, can you please write "name' "job position" "phone" "email" "address" on the card but leave them so I can add the details at a later time. Thank you. Also I plan on printing with UV spot printing as a background on the card. Keep this is mind when designing.

Thanks again.

Hello designers, please do not include pics of houses, house plansĀ or construction machinery etc as we really do not like the way it looks. Thank you.

Target Market(s)

Real Estate Agents, Land Owners, Local Council Departments, Govt Bodies, other Developers etc.

Industry/Entity Type

Business

Requirements
Must have
• 2-sided design with one side displaying our logo by itself and the other with the required info, such as name, address, tel no., email, abn etc.

```html
<!DOCTYPE html>
<html lang="en">
<head>
<meta charset="utf-8">
<title>Kestrelmoor Holdings – Business Card</title>
<link rel="stylesheet" href="https://fonts.googleapis.com/css2?family=Source+Sans+3:wght@400;700&display=swap">
<style>
  :root {
    --page-bg: #ffffff;
    --card-edge: #a9a9a9;
    --brand-red: #c0242b;
    --brand-blue: #23408e;
    --blue-light: #2bb8ee;
    --blue-mid: #1f6fc0;
    --blue-deep: #1e2a78;
    --text-light: #ffffff;
    --divider: rgba(255,255,255,0.55);
  }
  html, body {
    margin: 0;
    padding: 0;
    width: 1200px;
    height: 901px;
    overflow: hidden;
    background: var(--page-bg);
    font-family: "Source Sans 3", "Myriad Pro", Arial, sans-serif;
  }
  .canvas {
    position: relative;
    width: 1200px;
    height: 901px;
  }
  .card {
    position: absolute;
    width: 727px;
    height: 456px;
    box-sizing: border-box;
    border: 1px solid var(--card-edge);
  }
  .card--back {
    left: 427px;
    top: 402px;
    overflow: hidden;
  }
  .card--front {
    left: 46px;
    top: 50px;
    background: var(--page-bg);
    display: flex;
    align-items: center;
    justify-content: center;
    z-index: 2;
  }
  .brand {
    display: flex;
    flex-direction: column;
    align-items: center;
    gap: 18px;
    margin-top: -6px;
  }
  .brand__dot {
    width: 112px;
    height: 112px;
    border-radius: 50%;
    background: var(--brand-blue);
  }
  .brand__name {
    font-weight: 700;
    font-size: 34px;
    letter-spacing: 0.5px;
    color: var(--brand-red);
    white-space: nowrap;
  }
  .back__surface {
    position: absolute;
    inset: 0;
    background:
      radial-gradient(ellipse at 0% 100%, var(--blue-light) 0%, rgba(43,184,238,0) 55%),
      linear-gradient(100deg, var(--blue-mid) 0%, #2453b0 55%, var(--blue-deep) 100%);
  }
  .details {
    position: absolute;
    left: 0;
    right: 0;
    top: 306px;
    text-align: center;
    color: var(--text-light);
  }
  .details__name {
    font-size: 22px;
    margin: 0 0 18px;
  }
  .details__role {
    font-size: 14px;
  }
  .details__row {
    display: flex;
    justify-content: center;
    align-items: center;
    font-size: 20.5px;
    margin: 0 0 10px;
  }
  .details__sep {
    display: inline-block;
    width: 1px;
    height: 27px;
    background: var(--divider);
    margin: 0 14px;
  }
  .details__abn {
    font-size: 14.5px;
  }
  .details__row--second {
    padding-left: 10px;
  }
</style>
</head>
<body>
<div class="canvas">
  <section class="card card--back">
    <div class="back__surface" role="img" aria-label="Blue gradient background with a faint repeating brand-mark pattern for UV spot printing"></div>
    <div class="details">
      <p class="details__name">Liam Carrow <span class="details__role">- director</span></p>
      <p class="details__row">
        <span>03 9412 7730</span>
        <span class="details__sep"></span>
        <span>48 Halden Road&nbsp; Ashbury Vic 3871</span>
      </p>
      <p class="details__row details__row--second">
        <span>liam@kestrelmoor.com.au</span>
        <span class="details__sep"></span>
        <span class="details__abn">abn. 61 204 735 918</span>
      </p>
    </div>
  </section>

  <section class="card card--front">
    <div class="brand">
      <div class="brand__dot"></div>
      <div class="brand__name">KESTRELMOOR HOLDINGS</div>
    </div>
  </section>
</div>
</body>
</html>
```